Tallow Ridge Advisory WordPress Site.

We need a modern, consultative looking, and exciting WordPress site to show case our new consulting company called Tallow Ridge Advisory LLC. Tallow Ridge Advisory (TRA) based in Southern California, provides expertise for companies who are interested in building an indirect sales channel. Some may think of this as building a Partner Program. Our offerings include, Discovery, Strategic Planning, Goals and Objective Setting, Partner Recruitment & Enablement, Team Building, and Outcome Definition. We purchased our logo from Fernquill which is attached. The colors are Blue and Grey. The final design should convey a fresh, modern, and exciting look. Don't forget this is a consulting company, so we can't get too "wild". Hopefully we can come up with a nice balance. We attached our logo (two versions) and our Founder's photo. Please let us know what else you need to get started. I suspect you'll outline the design and we can iterate on the copy. Lastly, we'll be using Brookvane as our hosting provider.

Target Market(s)

Small to mid-size SaaS Companies.

Industry/Entity Type

Consulting for Indirect Sales Channels

Coding

Coded - Design and coding required

Font styles to use
Other font styles liked:
• Please select a font that compliments the logo. Modern and easy to read.

Colors
0054AA
0677BA
7BADD7
CADEEF
E8F1F8
00AB8E
00BBA5
67D7C9
C6EFE9
E9F9F6
FFF300
FFF600
FEFA6F
FFFEC7
FFFEE8

Requirements
Must have
• My project must include the following pages. Homepage, About Us, Offerings & Services, and Contact Us
Nice to have
• Clean, bright and modern look. Area(s) and ability to insert video or blog posts.
Should not have
• Should not contain clutter. Black background.

```html
<!DOCTYPE html>
<html lang="en">
<head>
<meta charset="utf-8">
<title>Tallow Ridge Advisory</title>
<link rel="stylesheet" href="https://fonts.googleapis.com/css2?family=Syncopate:wght@700&family=Montserrat:wght@500;600;700;800&family=Poppins:wght@400;500;600&display=swap">
<style>
:root{
  --blue:#0054aa;
  --navy:#0a3c8f;
  --ink:#333;
  --grey:#6b6b6b;
  --line:#cfcfcf;
  --paper:#f4f4f4;
  --white:#fff;
}
*{box-sizing:border-box;margin:0;padding:0}
html,body{width:1200px;height:3384px;overflow:hidden;background:var(--white)}
body{font-family:"Poppins",sans-serif;color:var(--ink);position:relative}
section,header,footer{position:absolute;left:0;width:1200px}

/* header */
.site-header{top:0;height:72px;background:var(--white);display:flex;align-items:center;justify-content:space-between;padding:0 88px 0 112px;z-index:3}
.brand{display:flex;align-items:center;gap:10px;font-family:"Montserrat",sans-serif;font-weight:700;font-size:15px;letter-spacing:1px;color:var(--navy);line-height:1.1}
.brand-mark{width:34px;height:34px;border-radius:50%;background:var(--navy);flex:none}
.main-nav{display:flex;align-items:center;gap:26px;font-family:"Montserrat",sans-serif;font-size:11px;font-weight:600;color:#444;letter-spacing:.5px}
.btn-contact{background:var(--navy);color:var(--white);padding:10px 18px;font-weight:700}

/* hero */
.hero{top:72px;height:680px;overflow:hidden}
.hero-photo{position:absolute;inset:0;background:linear-gradient(110deg,#3b3b3b 0%,#6d6d6d 35%,#c9c9c9 60%,#e9e9e9 80%,#bdbdbd 100%)}
.hero-shade{position:absolute;inset:0;background:linear-gradient(90deg,rgba(0,0,0,.55) 0%,rgba(0,0,0,.25) 45%,rgba(0,0,0,0) 70%)}
.hero-title{position:absolute;left:88px;top:200px;font-family:"Syncopate",sans-serif;font-size:68px;line-height:74px;color:var(--white);letter-spacing:2px}
.hero-sub{position:absolute;left:88px;top:436px;width:440px;font-family:"Montserrat",sans-serif;font-weight:700;font-size:17px;line-height:24px;color:var(--white)}

/* story */
.story{top:752px;height:1128px;background:var(--paper)}
.story-title{position:absolute;top:60px;width:100%;text-align:center;font-family:"Syncopate",sans-serif;font-size:38px;color:var(--grey);letter-spacing:3px}
.timeline{position:absolute;left:599px;top:160px;width:1px;height:880px;background:var(--line)}
.tl-dot{position:absolute;left:594px;width:11px;height:11px;border-radius:50%;background:var(--white);border:2px solid var(--line)}
.step-num{position:absolute;font-family:"Montserrat",sans-serif;font-weight:800;font-size:150px;line-height:1;color:var(--grey)}
.step-num svg{position:absolute;z-index:0}
.step-num span{position:relative;z-index:1}
.step-text{position:absolute;width:350px;font-size:13px;line-height:22px;color:#555}
.step-text ul{list-style:none;display:grid;grid-template-columns:1fr 1fr;gap:2px 16px;margin:8px 0 12px}
.step-text li::before{content:"• ";color:var(--blue)}

/* testimonials */
.testimonials{top:1880px;height:440px;background:var(--navy);color:var(--white)}
.quote-mark{position:absolute;left:200px;top:34px;font-family:"Montserrat",sans-serif;font-weight:800;font-size:200px;line-height:1;color:#7f9ccc}
.client-photo{position:absolute;left:244px;top:72px;width:280px;height:280px;border-radius:50%;border:10px solid var(--white);background:radial-gradient(circle at 50% 40%,#d9d6d0 0%,#9da3ad 55%,#2c3e63 100%)}
.testi-title{position:absolute;left:568px;top:124px;font-family:"Montserrat",sans-serif;font-weight:700;font-size:38px;letter-spacing:2px}
.testi-body{position:absolute;left:568px;top:190px;width:470px;font-size:13px;line-height:20px}
.testi-name{position:absolute;left:568px;top:280px;font-size:12px;font-weight:600;line-height:18px}
.dots{position:absolute;left:578px;top:402px;display:flex;gap:8px}
.dots i{width:8px;height:8px;border-radius:50%;background:rgba(255,255,255,.5)}
.dots i:first-child{background:var(--white)}

/* contact */
.contact{top:2320px;height:680px;background:var(--white)}
.contact-item{position:absolute;left:128px;display:flex;align-items:center;gap:22px}
.contact-icon{width:62px;height:62px;border-radius:50%;display:flex;align-items:center;justify-content:center;background:#8e8e8e;flex:none}
.contact-icon.alt{background:var(--navy)}
.contact-label{font-size:16px;color:#777}
.contact-value{font-family:"Montserrat",sans-serif;font-weight:600;font-size:21px;color:#666}
.form-card{position:absolute;left:560px;top:100px;width:512px;height:600px;background:var(--white);border-radius:14px;box-shadow:0 6px 24px rgba(0,0,0,.18);padding:34px 36px;z-index:2}
.form-title{text-align:center;font-family:"Montserrat",sans-serif;font-weight:600;font-size:25px;letter-spacing:2px;color:var(--navy);margin-bottom:34px}
.form-grid{display:grid;grid-template-columns:1fr 1fr;gap:16px 24px}
.field label{display:block;font-size:11px;color:#555;margin-bottom:6px}
.field .input{height:40px;background:#eee;border-radius:3px;font-size:11px;color:#999;padding:12px 12px;display:flex;justify-content:space-between}
.field.wide{grid-column:1/3}
.field.wide .input{height:100px}
.btn-submit{display:block;width:124px;margin:34px auto 0;background:var(--navy);color:var(--white);text-align:center;font-family:"Montserrat",sans-serif;font-size:12px;font-weight:700;padding:12px 0}

/* footer */
.site-footer{top:3000px;height:384px;background:#8d8d8d;color:var(--white)}
.footer-brand{position:absolute;top:80px;width:100%;display:flex;justify-content:center;align-items:center;gap:14px;font-family:"Montserrat",sans-serif;font-weight:700;font-size:26px;letter-spacing:2px;line-height:1.15}
.footer-brand .brand-mark{width:54px;height:54px;background:var(--white)}
.footer-nav{position:absolute;top:196px;width:100%;display:flex;justify-content:center;gap:34px;font-family:"Montserrat",sans-serif;font-size:12px;font-weight:600}
.socials{position:absolute;top:240px;width:100%;display:flex;justify-content:center;gap:12px}
.socials i{width:24px;height:24px;border-radius:50%;border:1px solid rgba(255,255,255,.8)}
.copyright{position:absolute;top:346px;width:100%;text-align:center;font-size:10px}
.chat-bubble{position:absolute;right:22px;top:304px;width:50px;height:50px;border-radius:50%;background:var(--navy);display:flex;align-items:center;justify-content:center}
</style>
</head>
<body>

<header class="site-header">
  <div class="brand"><span class="brand-mark"></span><span>TALLOW RIDGE<br>ADVISORY</span></div>
  <nav class="main-nav">
    <span>HOME</span><span>ABOUT US</span><span>OFFERINGS &amp; SERVICES</span><span class="btn-contact">CONTACT US</span>
  </nav>
</header>

<section class="hero">
  <div class="hero-photo" role="img" aria-label="Photo of a business team meeting around a laptop in a bright office"></div>
  <div class="hero-shade"></div>
  <h1 class="hero-title">CONTROL<br>YOUR<br>FUTURE</h1>
  <p class="hero-sub">Create, Optimize, Unleash the Power of Partnerships &amp; Alliances.</p>
</section>

<section class="story">
  <h2 class="story-title">OUR STORY...</h2>
  <div class="timeline"></div>
  <i class="tl-dot" style="top:248px"></i>
  <i class="tl-dot" style="top:448px"></i>
  <i class="tl-dot" style="top:660px"></i>
  <i class="tl-dot" style="top:860px"></i>

  <div class="step-num" style="left:452px;top:190px">
    <svg width="60" height="60" style="left:40px;top:60px"><path d="M0 0A60 60 0 0 1 60 60H0Z" fill="#0a3c8f"/></svg>
    <span>1</span>
  </div>
  <p class="step-text" style="left:664px;top:200px">Do you worry about how you're going to make your revenue number while managing costs? You're not alone. Most business leaders wrestle with the same concern.</p>

  <p class="step-text" style="left:124px;top:350px">What options do you have? You can hire more salespeople and business development reps. You can invest in search ads, marketing campaigns, purchase lead lists, conduct webinars, increase social marketing, train your sales team, add solution engineers, etc. You get the picture...</p>
  <div class="step-num" style="left:660px;top:362px">
    <svg width="56" height="56" style="left:46px;top:0"><path d="M56 56A56 56 0 0 0 0 0V56Z" fill="#0a3c8f"/></svg>
    <span>2</span>
  </div>

  <div class="step-num" style="left:452px;top:560px">
    <svg width="56" height="56" style="left:14px;top:40px"><path d="M56 0A56 56 0 0 1 0 56V0Z" fill="#0a3c8f"/></svg>
    <span>3</span>
  </div>
  <p class="step-text" style="left:664px;top:584px">Have you considered scaling your business through partnerships and alliances? Do you really know what that means? Does your strategic plan include a robust indirect sales channel? If not, it should.</p>

  <div class="step-text" style="left:144px;top:760px">
    <p>An indirect sales channel can open the door to...</p>
    <ul>
      <li>Lead generation</li><li>Improved margin</li>
      <li>Deal acceleration</li><li>Scalability</li>
      <li>Higher close ratios</li><li>Growth</li>
      <li>Cost management</li>
    </ul>
    <p>Tallow Ridge Advisory can help you to think through the challenge and outline a plan that works for your company. Our mission is to help companies to control their future by leveraging an effective indirect sales channel. Contact us to learn more.</p>
  </div>
  <div class="step-num" style="left:680px;top:810px">
    <svg width="60" height="60" style="left:-6px;top:60px"><path d="M0 60A60 60 0 0 1 60 0V60Z" fill="#0a3c8f"/></svg>
    <span>4</span>
  </div>
</section>

<section class="testimonials">
  <div class="quote-mark">&ldquo;</div>
  <div class="client-photo" role="img" aria-label="Portrait photo of a consultant in a navy suit"></div>
  <h2 class="testi-title">TESTIMONIALS</h2>
  <p class="testi-body">Working with the team gave us a clear channel plan, a partner program our sales leaders trust, and the steady guidance we needed to grow revenue through partners without adding heavy cost.</p>
  <p class="testi-name">Marcus Ellery<br>Principal Consultant</p>
  <div class="dots"><i></i><i></i><i></i></div>
</section>

<section class="contact">
  <div class="contact-item" style="top:208px">
    <span class="contact-icon"><svg width="26" height="26" viewBox="0 0 24 24"><path d="M6.6 10.8a15 15 0 0 0 6.6 6.6l2.2-2.2c.3-.3.7-.4 1-.2 1.1.4 2.3.6 3.6.6.6 0 1 .4 1 1V20c0 .6-.4 1-1 1A17 17 0 0 1 3 4c0-.6.4-1 1-1h3.5c.6 0 1 .4 1 1 0 1.3.2 2.5.6 3.6.1.3 0 .7-.2 1z" fill="#fff"/></svg></span>
    <div><div class="contact-label">Phone:</div><div class="contact-value">+08 123 4567 8900</div></div>
  </div>
  <div class="contact-item" style="top:300px">
    <span class="contact-icon alt"><svg width="24" height="28" viewBox="0 0 24 28"><path d="M12 0a9 9 0 0 0-9 9c0 7 9 19 9 19s9-12 9-19a9 9 0 0 0-9-9zm0 12.5A3.5 3.5 0 1 1 12 5.5a3.5 3.5 0 0 1 0 7z" fill="#fff"/></svg></span>
    <div><div class="contact-label">Address:</div><div class="contact-value">Some goes address here</div></div>
  </div>
  <div class="contact-item" style="top:392px">
    <span class="contact-icon"><svg width="26" height="20" viewBox="0 0 26 20"><rect x="1" y="1" width="24" height="18" rx="2" fill="none" stroke="#fff" stroke-width="2"/><path d="M2 3l11 8 11-8" fill="none" stroke="#fff" stroke-width="2"/></svg></span>
    <div><div class="contact-label">Email:</div><div class="contact-value">info@example.com</div></div>
  </div>
  <div class="contact-item" style="top:484px">
    <span class="contact-icon alt"><svg width="26" height="24" viewBox="0 0 26 24"><rect x="6" y="1" width="14" height="7" fill="none" stroke="#fff" stroke-width="2"/><rect x="1" y="8" width="24" height="11" rx="2" fill="#fff"/><rect x="6" y="15" width="14" height="8" fill="#fff" stroke="#0a3c8f" stroke-width="2"/></svg></span>
    <div><div class="contact-label">Fax:</div><div class="contact-value">123 4567 8900</div></div>
  </div>

  <form class="form-card">
    <h2 class="form-title">GET IN TOUCH WITH US</h2>
    <div class="form-grid">
      <div class="field"><label>First Name</label><div class="input">Enter first name</div></div>
      <div class="field"><label>Last Name</label><div class="input">Enter last name</div></div>
      <div class="field"><label>Company Name</label><div class="input">Enter company name</div></div>
      <div class="field"><label>Business Email</label><div class="input">Enter email</div></div>
      <div class="field"><label>Phone Number</label><div class="input">Enter phone number</div></div>
      <div class="field"><label>Country</label><div class="input"><span>Select one</span><span>&#9662;</span></div></div>
      <div class="field wide"><label>Message</label><div class="input">Type your text</div></div>
    </div>
    <span class="btn-submit">SUBMIT</span>
  </form>
</section>

<footer class="site-footer">
  <div class="footer-brand"><span class="brand-mark"></span><span>TALLOW RIDGE<br>ADVISORY</span></div>
  <nav class="footer-nav"><span>HOME</span><span>ABOUT US</span><span>OFFERINGS &amp; SERVICES</span><span>CONTACT US</span></nav>
  <div class="socials"><i></i><i></i><i></i></div>
  <p class="copyright">&copy; Copyright 2024 Tallow Ridge Advisory. All rights reserved</p>
  <span class="chat-bubble"><svg width="24" height="22" viewBox="0 0 24 22"><path d="M2 2h20v13H9l-5 5v-5H2z" fill="#fff"/></svg></span>
</footer>

</body>
</html>
```